Inpatient and outpatient services for people who have undergone urinary and faecal diversions.
Ross Halloway
Clinical Nurse Consultant Stomal Therapy
C/o K7d Surgical Unit
Brackenridge Hospital
Brackenridge 2198
P: 0412 375 804
P: 9721 3068 Pager: 41836
AS: 9721 4230 Clear writing and colour as people who read this may have vision problems
Information transfer about contact details, position of clinic, what to bring on follow up appointmants.

Target Market(s)

patients and staff to contact

Industry/Entity Type

Medical

Contact Information for Business Card

As above in Project description. Can use both sides.

Font styles to use
Decorative

Requirements
Must have
• Clear easy to read writing as patients may have eyesight problems
Nice to have
• Catchy colour & design

```html
<!DOCTYPE html>
<html lang="en">
<head>
<meta charset="utf-8">
<title>Ross Halloway – Business Card</title>
<link rel="stylesheet" href="https://fonts.googleapis.com/css2?family=Roboto:wght@300;400;700&family=Roboto+Condensed:wght@700&display=swap">
<style>
  :root {
    --backdrop: #e4e4e6;
    --card-white: #ffffff;
    --silver-light: #ececec;
    --silver-mid: #d2d2d2;
    --silver-dark: #bdbdbd;
    --ink: #111111;
    --ink-soft: #2a2a2a;
    --muted: #8c8c8c;
    --rule: #1a1a1a;
  }
  * { margin: 0; padding: 0; box-sizing: border-box; }
  html, body {
    width: 1200px;
    height: 800px;
    overflow: hidden;
    background: var(--backdrop);
    font-family: "Roboto", Arial, sans-serif;
  }
  .sheet {
    position: relative;
    width: 1200px;
    height: 800px;
    display: flex;
    align-items: center;
    justify-content: center;
    gap: 60px;
  }
  .card {
    position: relative;
    width: 525px;
    height: 300px;
    box-shadow: 0 6px 18px rgba(0,0,0,0.12), 0 1px 3px rgba(0,0,0,0.1);
  }

  /* Contact face */
  .card--contact {
    background: var(--card-white);
    color: var(--ink);
  }
  .identity {
    position: absolute;
    left: 34px;
    top: 40px;
  }
  .identity__name {
    font-weight: 700;
    font-size: 21px;
    letter-spacing: 0.2px;
    text-transform: uppercase;
    color: var(--ink);
  }
  .identity__role {
    font-weight: 300;
    font-size: 14.5px;
    color: var(--muted);
    margin-top: 2px;
  }
  .rule {
    position: absolute;
    height: 1.5px;
    background: var(--rule);
  }
  .rule--top { left: 34px; top: 96px; width: 290px; }
  .rule--address { right: 34px; top: 196px; width: 200px; }
  .contacts {
    position: absolute;
    left: 34px;
    top: 110px;
    list-style: none;
    font-size: 15px;
    line-height: 21px;
    color: var(--ink-soft);
  }
  .contacts li { display: flex; align-items: center; gap: 6px; }
  .contacts .icon { width: 11px; height: 11px; fill: var(--muted); }
  .contacts .label { color: var(--muted); }
  .contacts .divider { margin: 0 6px; color: var(--ink); }
  .address {
    position: absolute;
    right: 34px;
    top: 206px;
    width: 200px;
    font-size: 15.5px;
    line-height: 20px;
    color: var(--ink);
  }

  /* Name face */
  .card--name {
    background: radial-gradient(ellipse at 60% 45%, var(--silver-light) 0%, var(--silver-mid) 65%, var(--silver-dark) 100%);
    display: flex;
    align-items: center;
    justify-content: center;
  }
  .headline { text-align: left; }
  .headline__name {
    font-family: "Roboto", Arial, sans-serif;
    font-weight: 700;
    font-size: 50px;
    line-height: 1;
    letter-spacing: 0.5px;
    color: var(--ink);
  }
  .headline__role {
    font-family: "Roboto Condensed", "Arial Narrow", sans-serif;
    font-weight: 700;
    font-size: 14.5px;
    letter-spacing: 0.6px;
    text-transform: uppercase;
    color: var(--ink);
    margin-top: 2px;
  }
</style>
</head>
<body>
<main class="sheet">
  <section class="card card--contact" aria-label="Contact side">
    <div class="identity">
      <h1 class="identity__name">Ross Halloway</h1>
      <p class="identity__role">Clinical Nurse Consultant Stomal Therapy</p>
    </div>
    <div class="rule rule--top"></div>
    <ul class="contacts">
      <li>
        <svg class="icon" viewBox="0 0 24 24" aria-hidden="true"><path d="M6.6 10.8a15.1 15.1 0 0 0 6.6 6.6l2.2-2.2c.3-.3.7-.4 1-.2 1.1.4 2.3.6 3.6.6.6 0 1 .4 1 1V20c0 .6-.4 1-1 1A17 17 0 0 1 3 4c0-.6.4-1 1-1h3.5c.6 0 1 .4 1 1 0 1.3.2 2.5.6 3.6.1.3 0 .7-.2 1z"/></svg>
        <span>0412 375 804</span>
      </li>
      <li>
        <svg class="icon" viewBox="0 0 24 24" aria-hidden="true"><path d="M6.6 10.8a15.1 15.1 0 0 0 6.6 6.6l2.2-2.2c.3-.3.7-.4 1-.2 1.1.4 2.3.6 3.6.6.6 0 1 .4 1 1V20c0 .6-.4 1-1 1A17 17 0 0 1 3 4c0-.6.4-1 1-1h3.5c.6 0 1 .4 1 1 0 1.3.2 2.5.6 3.6.1.3 0 .7-.2 1z"/></svg>
        <span>9721 3068</span>
      </li>
      <li>
        <span><span class="label">Pager:</span> 41836<span class="divider">|</span><span class="label">AS:</span> 9721 4230</span>
      </li>
    </ul>
    <div class="rule rule--address"></div>
    <address class="address" style="font-style: normal;">
      C/o K7d Surgical Unit<br>
      Brackenridge Hospital<br>
      Brackenridge 2198
    </address>
  </section>

  <section class="card card--name" aria-label="Name side">
    <div class="headline">
      <h2 class="headline__name">ROSS HALLOWAY</h2>
      <p class="headline__role">Clinical Nurse Consultant Stomal Therapy</p>
    </div>
  </section>
</main>
</body>
</html>
```